HOLLOWBRIM BASH 2014 - Halloween Party

I need a 8.5x11 poster that can also be a jpeg for facebook and run as a display ad in print. I would like a facebook cover and profile picture that matches the poster. This is our 8th annual Halloween costume party and is our biggest event of the year.

Copy is as follows: (no particular order

8th Annual HOLLOWBRIM BASH
Halloween Costume Party
FRIDAY October 31st (need to emphasize date, usually I do it on Saturday.)
$400 in CASH PRIZES awarded at 9pm AND Midnight
DJ 7pm-2am in the tavern
Live music by VELVET RAVENS in the back room. 9pm.
Drink Specials, Munchies
$5 cover in advance, $10 at the door.
Cedarfield Lodge Inn, 4185 County Road 61, Larkhaven, NW

Target Market(s)

We are a bar and we have live music and a DJ for this party and are awarding for prizes for the best costumes (and other costumer categories.)

Industry/Entity Type

House

Font styles to use
Other font styles liked:
• halloween, spooky but readable

Requirements
Must have
• Must communicate the details clearly, be able to read from a distance. Due to the amount of Information we need to convey, I am willng to go 8x14 poster size. The emphasis should really be on "Hollowbrim Bash". "8th annual" is not very important and should be weighted less than Hollowbrim Bash.
Should not have
• shouldn't be too scary. I've had shop owners tell me that some are too scary to hang in their stores.

```html
<!DOCTYPE html>
<html lang="en">
<head>
<meta charset="utf-8">
<title>Hollowbrim Bash 2014 – Halloween Costume Party</title>
<link rel="stylesheet" href="https://fonts.googleapis.com/css2?family=Creepster&family=Montserrat:wght@600;700;800&family=Rubik+Distressed&display=swap">
<style>
  :root {
    --night-deep: #0a1320;
    --night-mid: #1d3140;
    --night-teal: #3c5a63;
    --castle-glow: #8a7a55;
    --blood-red: #e0231b;
    --blood-dark: #8e0d0a;
    --ghost-white: #f4f4f2;
  }
  * { margin: 0; padding: 0; box-sizing: border-box; }
  html, body { width: 927px; height: 1200px; overflow: hidden; background: var(--night-deep); }
  .poster {
    position: relative;
    width: 927px;
    height: 1200px;
    overflow: hidden;
    color: var(--ghost-white);
    font-family: "Montserrat", Arial, sans-serif;
  }
  .night-scene {
    position: absolute; inset: 0;
    background:
      radial-gradient(circle at 371px 271px, #e8e6dc 0 38px, rgba(200,210,210,0.35) 42px, rgba(80,110,120,0) 140px),
      radial-gradient(ellipse 260px 320px at 230px 680px, rgba(138,122,85,0.55), rgba(60,90,99,0) 100%),
      radial-gradient(ellipse 600px 500px at 420px 560px, rgba(60,90,99,0.75), rgba(29,49,64,0) 100%),
      linear-gradient(180deg, var(--night-deep) 0%, var(--night-mid) 40%, #223640 70%, var(--night-deep) 100%);
  }
  .centered { position: absolute; left: 0; width: 100%; text-align: center; white-space: nowrap; }
  .edition {
    position: absolute; left: 267px; top: 64px;
    font-weight: 700; font-size: 38px; letter-spacing: 1px;
    font-variant: small-caps;
  }
  .event-title {
    position: absolute; left: 0; top: 92px; width: 100%;
    font-family: "Creepster", "Impact", fantasy;
    font-weight: 400; color: var(--blood-red);
    line-height: 1;
    white-space: nowrap;
    text-shadow: 0 4px 0 var(--blood-dark), 0 0 14px rgba(0,0,0,0.6);
  }
  .event-title .line-one { display: block; padding-left: 87px; font-size: 170px; }
  .event-title .line-two { display: block; padding-left: 513px; font-size: 175px; letter-spacing: 4px; margin-top: -48px; }
  .party-type { top: 432px; font-size: 62px; }
  .party-type .holiday { font-family: "Creepster", fantasy; color: var(--blood-red); letter-spacing: 2px; }
  .party-type .kind { font-weight: 700; font-variant: small-caps; font-size: 58px; }
  .event-date {
    top: 500px; font-weight: 700; font-size: 56px;
    font-variant: small-caps; letter-spacing: -0.5px;
  }
  .prize-amount { top: 625px; font-family: "Rubik Distressed", "Impact", fantasy; font-size: 48px; letter-spacing: 1px; }
  .prize-amount .money { color: var(--blood-red); }
  .prize-times { top: 698px; font-weight: 700; font-size: 23px; font-variant: small-caps; }
  .lineup { top: 757px; font-weight: 700; font-size: 33px; line-height: 38px; font-variant: small-caps; }
  .lineup .upper { text-transform: uppercase; }
  .extras { top: 975px; color: var(--blood-red); font-weight: 700; font-size: 28px; line-height: 37px; font-variant: small-caps; }
  .venue { top: 1096px; font-weight: 700; font-size: 22px; font-variant: small-caps; letter-spacing: 0.5px; }
</style>
</head>
<body>
<main class="poster">
  <div class="night-scene" role="img" aria-label="Night scene of a castle on a misty hill under a full moon with flying bats and silhouetted hands below"></div>

  <p class="edition">8TH Annual</p>
  <h1 class="event-title">
    <span class="line-one">HOLLOWBRIM</span>
    <span class="line-two">BASH</span>
  </h1>

  <p class="centered party-type"><span class="holiday">HALLOWEEN</span> <span class="kind">Costume Party</span></p>
  <p class="centered event-date">FRIDAY October 31st</p>

  <p class="centered prize-amount"><span class="money">$400</span> IN CASH PRIZES</p>
  <p class="centered prize-times">Awarded at 9PM AND Midnight</p>

  <p class="centered lineup">
    DJ 7PM–2AM in the Tavern<br>
    Live music by <span class="upper">Velvet Ravens</span><br>
    in the back room at 9PM.
  </p>

  <p class="centered extras">
    Drink Specials, &nbsp;Munchies<br>
    $5 cover in advance, &nbsp;$10 at the door.
  </p>

  <p class="centered venue">Cedarfield Lodge Inn, &nbsp;4185 County Road 61, &nbsp;Larkhaven, &nbsp;NW</p>
</main>
</body>
</html>
```